Call A for Admission - Indpendent Radio Producer Needs a Poster Designed.

I've set-up a 1800 number connected to an answering machine, where people can call-in and make an Midnight Ledger.
I need a poster designed that will communicate the idea simply and entice people to call in.
Text to be included in the poster as follows:
This is the text I would like added:
Done something you regret?
Want to fess up, get it off your chest?
Call 1800 472 306 to make an Midnight Ledger.
It's free, feel good - and a lovely way to start the new year afresh!
Target Market(s)
Broad - ideally will appeal to a wide (adult) audience.
Industry/Entity Type
Radio
Look and feel

```html
<!DOCTYPE html>
<html lang="en">
<head>
<meta charset="utf-8">
<title>Midnight Ledger – Call Right Now</title>
<link href="https://fonts.googleapis.com/css2?family=Teko:wght@300;400;500&family=Dancing+Script:wght@600&display=swap" rel="stylesheet">
<style>
  :root {
    --paper: #eef0f1;
    --paper-glow: #ffffff;
    --mist: #d9dcde;
    --ink: #2f3236;
    --ink-soft: #55595e;
    --red: #c8171d;
    --red-bright: #e52a2e;
    --red-deep: #8e0e12;
    --band: #2a2c2f;
    --band-soft: #4a4d52;
    --highlight: #ffd21f;
    --rule: #8a8d90;
    --chrome: #f7f7f7;
    --chrome-shade: #d7d9db;
    --shadow: #9a9da0;
  }
  * { margin: 0; padding: 0; box-sizing: border-box; }
  html, body { width: 816px; height: 1200px; overflow: hidden; }
  body {
    background: var(--paper);
    font-family: "Teko", "Arial Narrow", sans-serif;
  }
  .poster {
    position: relative;
    width: 816px;
    height: 1200px;
    overflow: hidden;
    background:
      radial-gradient(circle at 12% 20%, var(--paper-glow) 0 40px, transparent 80px),
      radial-gradient(circle at 88% 14%, var(--paper-glow) 0 50px, transparent 100px),
      radial-gradient(circle at 90% 60%, var(--paper-glow) 0 36px, transparent 80px),
      radial-gradient(circle at 8% 70%, var(--paper-glow) 0 30px, transparent 70px),
      radial-gradient(ellipse at 50% 50%, var(--paper-glow) 0%, var(--paper) 55%, var(--mist) 100%);
  }
  .presenter {
    position: absolute;
    top: 6px; left: 0; right: 0;
    text-align: center;
    color: var(--ink);
    line-height: 1;
  }
  .presenter-person {
    font-family: "Dancing Script", cursive;
    font-size: 14px;
  }
  .presenter-station {
    font-size: 20px;
    font-weight: 500;
    letter-spacing: 1.5px;
    text-transform: uppercase;
    margin-top: 1px;
  }
  .presenter-verb {
    font-size: 19px;
    font-weight: 400;
    letter-spacing: 1.5px;
    text-transform: uppercase;
    color: var(--ink-soft);
  }
  .hero-art {
    position: absolute;
    left: 48px; top: 100px;
    width: 720px; height: 820px;
    background:
      radial-gradient(ellipse 32% 28% at 50% 63%, var(--red-bright) 0%, var(--red) 55%, var(--red-deep) 85%, transparent 100%),
      radial-gradient(ellipse 46% 40% at 50% 56%, var(--band) 0%, var(--band-soft) 60%, transparent 100%),
      radial-gradient(ellipse 50% 48% at 50% 50%, var(--chrome) 0%, var(--chrome-shade) 70%, transparent 100%);
  }
  .hero-mark {
    position: absolute;
    left: 0; right: 0; top: 565px;
    text-align: center;
    font-size: 170px;
    font-weight: 400;
    color: #ffffff;
    line-height: 1;
  }
  .cta-kicker {
    position: absolute;
    top: 186px; left: 0; right: 0;
    text-align: center;
    font-size: 15px;
    font-weight: 500;
    letter-spacing: 1px;
    color: var(--ink);
    text-transform: uppercase;
  }
  .title {
    position: absolute;
    left: 0; right: 0;
    text-align: center;
    text-transform: uppercase;
    line-height: 1;
  }
  .title-top {
    top: 200px;
    font-size: 150px;
    font-weight: 300;
    letter-spacing: 4px;
    color: var(--chrome);
    text-shadow: 0 2px 0 var(--shadow), 0 4px 6px rgba(0,0,0,.25);
  }
  .title-bottom {
    top: 350px;
    font-size: 138px;
    font-weight: 500;
    letter-spacing: 3px;
    color: var(--red);
    text-shadow: 0 2px 0 var(--red-deep), 0 4px 6px rgba(0,0,0,.25);
  }
  .rule {
    position: absolute;
    left: 80px; width: 646px; height: 1px;
    background: var(--rule);
  }
  .rule-top { top: 936px; }
  .rule-bottom { top: 1004px; }
  .copy {
    position: absolute;
    left: 0; right: 0;
    text-align: center;
    text-transform: uppercase;
    line-height: 1;
    white-space: nowrap;
  }
  .copy-question { top: 948px; font-size: 54px; font-weight: 400; color: var(--red); }
  .copy-invite { top: 1020px; font-size: 42px; font-weight: 400; color: var(--ink); }
  .copy-call { top: 1072px; font-size: 36px; font-weight: 400; color: var(--ink); }
  .copy-call .phone { color: var(--highlight); }
  .copy-closer { top: 1122px; font-size: 35px; font-weight: 400; color: var(--red); }
</style>
</head>
<body>
<main class="poster">
  <header class="presenter">
    <div class="presenter-person">Nora Whitfield</div>
    <div class="presenter-station">Late Line Radio</div>
    <div class="presenter-verb">Presenting</div>
  </header>

  <div class="hero-art" role="img" aria-label="White studio headphones wrapped around a glossy red heart"></div>
  <div class="hero-mark" aria-hidden="true">?</div>

  <p class="cta-kicker">Call right now !</p>
  <h1>
    <span class="title title-top">Midnight</span>
    <span class="title title-bottom">Ledger</span>
  </h1>

  <div class="rule rule-top"></div>
  <p class="copy copy-question">Done something you regret?</p>
  <div class="rule rule-bottom"></div>
  <p class="copy copy-invite">Want to fess up, get it off your chest?</p>
  <p class="copy copy-call">Call <span class="phone">1800 472 306</span> to make your Midnight Ledger !</p>
  <p class="copy copy-closer">It's free, feel good, and a lovely way to start the new year afresh !</p>
</main>
</body>
</html>
```